Personal Finance Author needs a postcard

Hi there,

I am a Canadian personal finance author and have published a new book called The Wealth Compass.

I teach Millennials how to create a 6-figure portfolio through investing (https://www.dariafelt.com/)

I'm speaking at some conferences so we were going to print some postcards to hand out to attendees with our info and calls-to-action on them.

I am looking for 4x6 (horizontal) postcard (no space needed for shipping label).

Logos, Headshots and Book Cover:
https://files.cloudvaultex.com/folders/8kQpZrT2mWvN4xLbJ7sHdYc3FgA9eUoRi?usp=sharing

Both sides will be full colour. I would like a clean and simple look. Our main sites are www.DariaFelt.com and www.TheWealthCompassBook.com if you want to get a sense of style and design.
I also uploaded a few marketing materials so you can see the existing designs.

Side 1:
Get Instant Access to your Free Resources - main headline

(small bullets underneath)
- The Wealth Compass Checklist
- Financial Worksheets
- Database of Investment Tools

DariaFelt.com/Resources

At the bottom, include "Don't forget to follow Daria Felt on social media:
Proflink: @dariafelt7
Friendhub: @thewealthcompassbook Photoline: @thewealthcompassbook Chatterly: @WealthCompassBk"

Side 2:
Headline - Want to work directly with Daria and The Wealth Compass team to help you make your money grow and stay safe?

Work with us to (bullet point list)...
- Hire Daria as a Keynote Speaker
- Teach Financial Literacy Workshops
- Receive Financial Coaching

Want To Learn More About How We Can Help?
DariaFelt.com/Services

Include my contact info:
Daria Felt
Author | Speaker | Investor
daria@thewealthcompassbook.com
416-555-0187

Target Market(s)

Millennials who want to learn how to save and invest their money. I focus on stock market investing, real estate investing and entrepreneurship.

Industry/Entity Type

Financial Service

Font styles to use
Sans Serif

Colors

Designer to choose colors to be used in the design.

Requirements
Must have
• Photo of Daria Felt
• The Wealth Compass logo
• Green, Gold/Yellow to match existing colours
• modern business style postcard

```html
<!DOCTYPE html>
<html lang="en">
<head>
<meta charset="utf-8">
<title>The Wealth Compass – Postcard</title>
<link rel="stylesheet" href="https://fonts.googleapis.com/css2?family=Arimo:wght@400;700&display=swap">
<style>
  :root {
    --green: #035f33;
    --gold: #ebb83e;
    --ink: #111111;
    --paper: #ffffff;
    --frame: #9a9a9a;
  }
  * { margin: 0; padding: 0; box-sizing: border-box; }
  html, body { width: 1200px; height: 1200px; overflow: hidden; background: var(--paper); }
  body { position: relative; font-family: "Arimo", Arial, sans-serif; color: var(--ink); }

  .card { position: absolute; width: 820px; height: 546px; background: var(--paper); border: 1px solid var(--frame); overflow: hidden; }
  .card-front { left: 32px; top: 28px; }
  .card-back { left: 339px; top: 623px; }
  .abs { position: absolute; white-space: nowrap; }

  /* Front */
  .resource-panel { position: absolute; left: 235px; top: 0; width: 339px; height: 458px; background: var(--gold); }
  .author-name { left: 34px; top: 31px; font-size: 25px; font-weight: 700; letter-spacing: 0.3px; }
  .book-title { left: 22px; top: 76px; width: 200px; text-align: center; font-size: 38px; line-height: 42px; font-weight: 700; color: var(--green); white-space: normal; }
  .book-stack { position: absolute; left: 34px; top: 228px; width: 170px; height: 256px; background: linear-gradient(160deg, #f1f1ee 0%, #d9dbd4 55%, #1f6b3f 100%); z-index: 2; }
  .author-photo { position: absolute; left: 586px; top: 28px; width: 226px; height: 430px; border-radius: 100px 100px 0 0; background: linear-gradient(180deg, #d6b8a0 0%, #2a2c3a 30%, #1b1d29 100%); }
  .headline { color: var(--green); font-weight: 700; font-size: 23.5px; line-height: 27px; letter-spacing: 0.3px; }
  .front-headline { left: 256px; top: 86px; }
  .bullets { list-style: none; }
  .bullets li { position: relative; padding-left: 20px; font-size: 21.5px; line-height: 34px; white-space: nowrap; }
  .bullets li::before { content: ""; position: absolute; left: 1px; top: 13px; width: 8px; height: 8px; border: 2px solid var(--green); }
  .front-bullets { left: 250px; top: 160px; }
  .resource-url { left: 272px; top: 404px; font-size: 22px; }
  .social-band { position: absolute; left: 0; top: 458px; width: 820px; height: 88px; background: var(--green); color: var(--paper); text-align: center; font-size: 20px; line-height: 24px; padding-top: 7px; padding-left: 190px; padding-right: 10px; }
  .social-band span + span { margin-left: 12px; }

  /* Back */
  .pitch-panel { position: absolute; left: 0; top: 0; width: 222px; height: 546px; background: var(--gold); }
  .pitch-stripe { position: absolute; left: 222px; top: 0; width: 53px; height: 546px; background: var(--green); }
  .pitch { position: absolute; right: 610px; top: 79px; text-align: right; font-size: 24px; line-height: 28.8px; font-weight: 700; letter-spacing: 0.3px; }
  .work-intro { left: 358px; top: 81px; font-size: 22px; }
  .back-bullets { left: 358px; top: 106px; }
  .back-bullets li { line-height: 25.5px; font-size: 22px; }
  .back-bullets li::before { top: 8px; }
  .back-headline { left: 358px; top: 210px; }
  .services-url { left: 358px; top: 293px; font-size: 23px; font-weight: 700; }
  .contact { left: 358px; top: 345px; font-size: 22px; line-height: 25px; }
  .contact strong { font-weight: 700; }
</style>
</head>
<body>

<section class="card card-front">
  <div class="resource-panel"></div>
  <div class="abs author-name">DARIA FELT</div>
  <div class="abs book-title">THE WEALTH COMPASS</div>
  <div class="book-stack" role="img" aria-label="Stack of copies of The Wealth Compass book with the author on the cover"></div>
  <div class="author-photo" role="img" aria-label="Portrait photo of Daria Felt in a dark blazer, hand on hip"></div>

  <h2 class="abs headline front-headline">GET INSTANT ACCESS TO<br>YOUR FREE RESOURCES</h2>
  <ul class="abs bullets front-bullets">
    <li>The Wealth Compass Checklist</li>
    <li>Financial Worksheets</li>
    <li>Database of Investment Tools</li>
  </ul>
  <div class="abs resource-url">DariaFelt.com/Resources</div>

  <div class="social-band">
    <div>Don't forget to follow Daria Felt on social media:</div>
    <div><span>Proflink: @dariafelt7</span><span>Friendhub: @thewealthcompassbook</span></div>
    <div><span>Photoline: @thewealthcompassbook</span><span>Chatterly: @WealthCompassBk</span></div>
  </div>
</section>

<section class="card card-back">
  <div class="pitch-panel"></div>
  <div class="pitch-stripe"></div>
  <h2 class="pitch">WANT TO<br>WORK<br>DIRECTLY<br>WITH DARIA<br>AND THE<br>WEALTH<br>COMPASS<br>TEAM TO<br>HELP YOU<br>MAKE YOUR<br>MONEY<br>GROW AND<br>STAY SAFE?</h2>

  <div class="abs work-intro">Work with us to :</div>
  <ul class="abs bullets back-bullets">
    <li>Hire Daria as a Keynote Speaker</li>
    <li>Teach Financial Literacy Workshops</li>
    <li>Receive Financial Coaching</li>
  </ul>
  <h2 class="abs headline back-headline">WANT TO LEARN MORE ABOUT<br>HOW WE CAN HELP?</h2>
  <div class="abs services-url">DariaFelt.com/Services</div>
  <div class="abs contact">
    <strong>Daria Felt</strong><br>
    Author | Speaker | Investor<br>
    daria@thewealthcompassbook.com<br>
    416-555-0187
  </div>
</section>

</body>
</html>
```